Chewing Gum With Active Ingredients Needs Packaging Design

Brivelle Gum Science is a revolutionary new chewing gum that contains active ingredients commonly found in mouthwashes - it's a portable and convenient way to keep a fresh, clean, and healthy mouth. We have a thorough design brief (attached file) for the packaging we need - a simple sleeve for blister packed gum. We want our design to convey that we are a modern, effective, and high-end product.

Target Market(s)

Young professionals, 20-35 years old

Font styles to use
Serif
Sans Serif

Colors
0292cd
ffffff
0555a3

Requirements
Must have
• A sleek, elegant design
• ALL of the elements listed in the creative brief PDF
• Attached logo
Nice to have
• Incorporation of foil into the design
• A unique, unmistakable look
Should not have
• Too medical of a look

```html
<!DOCTYPE html>
<html lang="en">
<head>
<meta charset="utf-8">
<title>Brivelle Gum Science – Peppermint Sleeve</title>
<link rel="stylesheet" href="https://fonts.googleapis.com/css2?family=Antonio:wght@300;400;500&display=swap">
<style>
  :root {
    --stage: #e9e9e9;
    --deep-teal: #06344a;
    --mid-teal: #0b5f80;
    --glow: #1a93b8;
    --white: #ffffff;
    --silver: #b9bcc0;
    --brand-blue: #0555a3;
    --brand-cyan: #0292cd;
    --mint-dark: #2f7d2a;
    --mint-light: #6cc24a;
    --font-display: "Antonio", "Arial Narrow", sans-serif;
  }
  * { box-sizing: border-box; margin: 0; padding: 0; }
  html, body { width: 1200px; height: 1200px; overflow: hidden; background: var(--stage); }
  .canvas { position: relative; width: 1200px; height: 1200px; }
  .sleeve {
    position: absolute; left: 80px; top: 245px; width: 1040px; height: 710px;
    overflow: hidden; font-family: var(--font-display); color: var(--white);
    background:
      radial-gradient(ellipse 60% 55% at 52% 55%, var(--glow) 0%, var(--mid-teal) 45%, var(--deep-teal) 100%);
  }
  .sleeve__art { position: absolute; inset: 0; }
  .brand {
    position: absolute; left: 556px; top: 90px; transform: translateX(-50%);
    display: flex; align-items: center; gap: 22px; color: var(--brand-blue);
    font-weight: 300; white-space: nowrap;
  }
  .brand__dot { width: 70px; height: 70px; border-radius: 50%; background: var(--brand-blue); }
  .brand__name { font-size: 72px; line-height: 1; letter-spacing: 6px; text-transform: uppercase; }
  .brand__tagline { font-size: 17px; letter-spacing: 17px; text-transform: uppercase; margin-top: 4px; }
  .claims {
    position: absolute; top: 362px; font-size: 50px; font-weight: 400;
    line-height: 52px; letter-spacing: 2px; text-transform: uppercase;
  }
  .claims--left { left: 129px; }
  .claims--right { left: 589px; }
  .flavour {
    position: absolute; left: 530px; top: 598px; transform: translateX(-50%);
    text-align: center; white-space: nowrap;
  }
  .flavour__name { font-size: 50px; font-weight: 400; letter-spacing: 14px; line-height: 1; }
  .flavour__facts { font-size: 15px; letter-spacing: 1.5px; margin-top: 6px; text-transform: uppercase; }
  .count { position: absolute; left: 932px; top: 578px; display: flex; align-items: center; gap: 8px; }
  .count__number { font-size: 92px; font-weight: 500; line-height: 1; }
  .count__label { font-size: 14px; line-height: 27px; text-transform: uppercase; letter-spacing: 0.5px; }
  .mint-leaves {
    position: absolute; left: 0; bottom: 0; width: 150px; height: 115px;
    border-top-right-radius: 90px 70px;
    background: radial-gradient(ellipse at 40% 60%, var(--mint-light), var(--mint-dark));
  }
</style>
</head>
<body>
<main class="canvas">
  <section class="sleeve">
    <svg class="sleeve__art" width="1040" height="710" viewBox="0 0 1040 710" aria-hidden="true">
      <defs>
        <linearGradient id="foil-edge" x1="0" y1="0" x2="1" y2="0">
          <stop offset="0" stop-color="#9ea2a7"/>
          <stop offset="0.5" stop-color="#e4e6e8"/>
          <stop offset="1" stop-color="#9ea2a7"/>
        </linearGradient>
        <linearGradient id="panel-white" x1="0" y1="0" x2="0" y2="1">
          <stop offset="0" stop-color="#ffffff"/>
          <stop offset="1" stop-color="#f1f2f3"/>
        </linearGradient>
      </defs>
      <path class="arc-foil" d="M88 0 A 472 306 0 0 0 1019 0 Z" fill="url(#foil-edge)"/>
      <path class="arc-panel" d="M97 0 A 463 294 0 0 0 1010 0 Z" fill="url(#panel-white)"/>
    </svg>

    <div class="brand">
      <span class="brand__dot"></span>
      <div>
        <div class="brand__name">Brivelle</div>
        <div class="brand__tagline">Gum Science</div>
      </div>
    </div>

    <div class="claims claims--left">
      <p>Whitens teeth</p>
      <p>Freshens breath</p>
    </div>
    <div class="claims claims--right">
      <p>Helps reduce plaque</p>
      <p>Helps protect gums</p>
    </div>

    <div class="mint-leaves" role="img" aria-label="Fresh peppermint leaves"></div>

    <div class="flavour">
      <p class="flavour__name">PEPPERMINT</p>
      <p class="flavour__facts">Sugar free gum &nbsp;|&nbsp; Aspartame free &nbsp;|&nbsp; With xylitol</p>
    </div>

    <div class="count">
      <span class="count__number">8</span>
      <span class="count__label">Pieces<br>Sugar free<br>Gum</span>
    </div>
  </section>
</main>
</body>
</html>
```